Poster of Core Values & Motto

Create our core values poster and motto. Attached are our core values and our Motto. This poster represents both of our companies Tidal Pulp & CarvoBin.

Target Market(s)

Our team / employees

Industry/Entity Type

Shredding and Medical Waste

Colors
59FF00
82FF00
B8FF75
E3FFCB
F4FFEA
EB3D1F
EC4F4E
F09395
F8D3D4
FCEDEE

Requirements
Must have
• Include both companies logos

```html
<!DOCTYPE html>
<html lang="en">
<head>
<meta charset="utf-8">
<title>Core Values Poster – Tidal Pulp &amp; CarvoBin</title>
<link rel="stylesheet" href="https://fonts.googleapis.com/css2?family=Montserrat:wght@900&family=Source+Sans+3:wght@400;600;700&display=swap">
<style>
  :root {
    --leaf: #93c01f;
    --ink: #231f20;
    --alert: #eb3d1f;
    --paper: #ffffff;
  }
  * { margin: 0; padding: 0; box-sizing: border-box; }
  html, body { width: 848px; height: 1200px; overflow: hidden; background: var(--paper); }
  .poster {
    position: relative;
    width: 848px;
    height: 1200px;
    background: var(--paper);
    font-family: "Source Sans 3", Arial, sans-serif;
    color: var(--leaf);
  }
  .value-title { font-weight: 700; font-size: 18px; line-height: 20px; letter-spacing: 0.2px; }
  .value-line { font-weight: 400; font-size: 18px; line-height: 20px; }
  .corner-value { position: absolute; top: 20px; }
  .corner-value--left { left: 47px; }
  .corner-value--right { right: 26px; text-align: right; }
  .side-value {
    position: absolute;
    transform-origin: 0 0;
    transform: rotate(-90deg);
    white-space: nowrap;
  }
  .side-value--synergy   { left: 18px;  top: 983px; }
  .side-value--efficient { left: 18px;  top: 514px; }
  .side-value--dependable{ left: 777px; top: 484px; }
  .side-value--secure    { left: 777px; top: 983px; }
  .pillars { position: absolute; left: 0; top: 0; }
  .pillar-word {
    font-family: "Montserrat", Arial, sans-serif;
    font-weight: 900;
    font-size: 178px;
    fill: var(--leaf);
  }
  .motto {
    position: absolute;
    top: 925px;
    left: 0;
    width: 848px;
    text-align: center;
    font-weight: 700;
    font-size: 22px;
    line-height: 27px;
    letter-spacing: 0.3px;
  }
  .divider-band {
    position: absolute;
    left: 0;
    top: 1007px;
    width: 848px;
    height: 26px;
    background: var(--leaf);
  }
  .brand {
    position: absolute;
    top: 1068px;
    display: flex;
    align-items: center;
    gap: 10px;
    font-weight: 700;
    font-size: 26px;
    line-height: 1;
  }
  .brand--pulp { left: 200px; color: var(--leaf); }
  .brand--bin  { left: 462px; color: var(--ink); }
  .brand-dot { width: 22px; height: 22px; border-radius: 50%; background: var(--leaf); }
  .brand-square { width: 20px; height: 20px; background: var(--alert); }
</style>
</head>
<body>
<main class="poster">
  <div class="corner-value corner-value--left">
    <div class="value-title">EXELLANCE</div>
    <div class="value-line">Exceed with a smile</div>
  </div>
  <div class="corner-value corner-value--right">
    <div class="value-title">HONESTY/INTEGRITY</div>
    <div class="value-line">Do the right thing</div>
  </div>

  <div class="side-value side-value--synergy">
    <div class="value-title">SYNERGY/TEAMWORK</div>
    <div class="value-line">Get It Done Attitude with Humble confidence</div>
  </div>
  <div class="side-value side-value--efficient">
    <div class="value-title">EFFICIENT</div>
    <div class="value-line">On-Time, sence of urgency, always trying to improve</div>
  </div>
  <div class="side-value side-value--dependable">
    <div class="value-title">DEPENDABLE</div>
    <div class="value-line">Do what you say you will do</div>
  </div>
  <div class="side-value side-value--secure">
    <div class="value-title">SAFE AND SECURE</div>
    <div class="value-line">We are just as secure as an armored truck with money</div>
  </div>

  <svg class="pillars" width="848" height="1200" viewBox="0 0 848 1200" aria-label="Purpose, Cause, Passion">
    <text class="pillar-word" transform="translate(343 842) rotate(-90)" textLength="736" lengthAdjust="spacingAndGlyphs">PURPOSE</text>
    <text class="pillar-word" transform="translate(474 842) rotate(-90)" textLength="454" lengthAdjust="spacingAndGlyphs">CAUSE</text>
    <text class="pillar-word" transform="translate(630 842) rotate(-90)" textLength="726" lengthAdjust="spacingAndGlyphs">PASSION</text>
  </svg>

  <div class="motto">REMIND PEOPLE<br>WHAT GREAT SERVICE LOOKS LIKE</div>

  <div class="divider-band"></div>

  <div class="brand brand--pulp"><span class="brand-dot"></span>Tidal Pulp</div>
  <div class="brand brand--bin"><span class="brand-square"></span>CarvoBin</div>
</main>
</body>
</html>
```